Political Mail Out Quintero front and back

Front
Esteban (9th Grade) Quintero!

What's that famous saying?

Show me who your friends are and I'll tell you who you really are!
(show the two guys)

Walter Cuellar is charged with voter fraud by changing voter addresses from across the RGV so they could vote in Edinburg
Back
Did Esteban (9th Grade) Quintero commit voter fraud when he ran for office in 2016?
(insert blurred photo)

Here is a list of people from all over the RGV that voted in Edinburg in the 2016 race.
Here is a break down:

(highlight the number and where they were first registered to vote)

9 People voted in Edinburg who were registered in Donna.
13 People voted in Edinburg who were registered in San Juan
8 People voted in Edinburg who were registered in Pharr
31 People voted in Edinburg who were registered in McAllen
2 People voted in Edinburg who were registered in La Joya
6 People voted in Edinburg who were registered in Edcouch
2 People voted in Edinburg who were registered in Mercedes
2 People voted in Edinburg who were registered in Monte Alto
6 People voted in Edinburg who were registered in Weslaco
1 Person voted in Edinburg who were registered in Penitas
3 People voted in Edinburg who were registered in Alamo
5 People voted in Edinburg who were registered in Elsa
6 People voted in Edinburg who were registered in Mission
1 Person voted in Edinburg who were registered in Alton

Will Esteban (9th Grade) Quintero CHEAT in 2020?

Only time will tell.

Vote Esteban (9th Grade) Quintero OUT of office.

```html
<!DOCTYPE html>
<html lang="en">
<head>
<meta charset="utf-8">
<title>Quintero Mail Out – Front and Back</title>
<link href="https://fonts.googleapis.com/css2?family=Poppins:wght@500;700;800&family=Barlow+Condensed:wght@600;700&family=Cabin:wght@400;600;700&display=swap" rel="stylesheet">
<style>
  :root {
    --navy: #0d2a63;
    --navy-deep: #0a1f4a;
    --blue: #1a4c9c;
    --gold: #f9b21b;
    --gold-dark: #d8900d;
    --paper: #ffffff;
    --page: #e4e5e7;
    --rule: #b9bcc4;
  }
  * { box-sizing: border-box; margin: 0; padding: 0; }
  html, body { width: 904px; height: 1200px; overflow: hidden; }
  body { background: var(--page); font-family: "Cabin", sans-serif; position: relative; }

  .card {
    position: absolute; left: 52px; width: 800px; height: 560px;
    background: var(--paper); overflow: hidden;
    box-shadow: 0 6px 18px rgba(0,0,0,.25);
  }
  .card--front { top: 30px; }
  .card--back { top: 610px; }
  .card > svg.shapes { position: absolute; inset: 0; }
  .abs { position: absolute; }

  .wordmark {
    font-family: "Poppins", sans-serif; font-weight: 800; color: var(--navy);
    text-align: center; line-height: 1; display: flex; align-items: center; gap: 10px;
  }
  .wordmark__dot { width: 14px; height: 14px; background: var(--gold); border-radius: 50%; flex: none; }
  .wordmark__name { font-size: 30px; line-height: 1.05; }

  /* front */
  .front__logo { left: 40px; top: 58px; width: 280px; justify-content: center; }
  .name-band { left: 30px; top: 190px; width: 290px; color: #fff; font-family: "Poppins", sans-serif; }
  .name-band__first { font-size: 26px; font-weight: 500; letter-spacing: .3px; }
  .name-band__last { font-size: 50px; font-weight: 800; color: var(--gold); line-height: 1.1; }
  .charge { left: 31px; top: 338px; width: 280px; color: var(--navy); font-size: 15.5px; line-height: 25.5px; font-weight: 600; }
  .socials { left: 57px; top: 464px; display: flex; gap: 21px; }
  .socials span { width: 28px; height: 28px; border: 2px solid var(--navy); border-radius: 50%; }
  .handle {
    left: 31px; top: 506px; width: 230px; height: 26px; border-radius: 13px;
    background: var(--navy); color: #fff; font-size: 12px; font-weight: 600;
    display: flex; align-items: center; justify-content: center;
  }
  .saying-q { right: 26px; top: 464px; color: #fff; font-family: "Barlow Condensed", sans-serif; font-weight: 700; font-size: 19px; letter-spacing: .3px; }
  .saying { right: 24px; top: 488px; width: 500px; text-align: right; color: var(--navy); font-family: "Barlow Condensed", sans-serif; font-weight: 700; font-size: 22px; line-height: 24px; }

  /* back */
  .back__question { left: 18px; top: 30px; width: 370px; text-align: center; color: var(--gold); font-family: "Poppins", sans-serif; font-weight: 500; font-size: 21px; line-height: 31px; }
  .back__list-photo {
    left: 16px; top: 116px; width: 78px; height: 94px; transform: rotate(-20deg);
    background: linear-gradient(135deg, #f4f4f4, #c9ccd3); box-shadow: 2px 3px 8px rgba(0,0,0,.45);
  }
  .back__intro { left: 118px; top: 146px; width: 260px; text-align: center; color: #fff; font-size: 13px; line-height: 20.5px; }
  .breakdown { left: 34px; top: 250px; list-style: none; color: #fff; font-size: 10.6px; line-height: 13px; }
  .breakdown strong { font-weight: 700; }
  .cheat { left: 31px; top: 448px; color: var(--navy); font-family: "Barlow Condensed", sans-serif; font-weight: 700; font-size: 18px; line-height: 23px; }
  .cheat span { display: block; font-family: "Cabin", sans-serif; font-size: 14px; font-weight: 700; }
  .vote-out { left: 36px; top: 518px; color: #fff; font-family: "Barlow Condensed", sans-serif; font-weight: 700; font-size: 19px; }
  .vote-out em { font-style: normal; color: var(--gold); }
  .back__logo { left: 450px; top: 58px; width: 190px; justify-content: center; }
  .stamp { left: 663px; top: 25px; width: 110px; height: 84px; border: 1.5px solid var(--rule); }
  .address-line { left: 440px; width: 333px; height: 1.5px; background: var(--rule); }
</style>
</head>
<body>

<section class="card card--front" aria-label="Mailer front">
  <svg class="shapes" width="800" height="560" viewBox="0 0 800 560">
    <defs>
      <linearGradient id="photoTone" x1="0" y1="0" x2="1" y2="1">
        <stop offset="0" stop-color="#6b4a2e"/>
        <stop offset=".5" stop-color="#9b6a4b"/>
        <stop offset="1" stop-color="#4d4f55"/>
      </linearGradient>
    </defs>
    <rect x="0" y="0" width="800" height="560" fill="#f1f2f4"/>
    <g role="img" aria-label="Photo of the candidate smiling arm in arm with Walter Cuellar">
      <polygon points="366,0 800,0 800,450 318,450" fill="url(#photoTone)"/>
    </g>
    <rect x="366" y="0" width="434" height="50" fill="#050505"/>
    <polygon points="318,450 800,450 800,560 330,560 300,500" fill="var(--navy)"/>
    <polygon points="0,176 336,176 320,326 0,326" fill="var(--blue)"/>
    <polygon points="336,176 350,176 330,326 320,326" fill="var(--navy-deep)"/>
    <polygon points="0,326 320,326 322,332 0,332" fill="var(--navy-deep)" opacity=".5"/>
    <polygon points="290,482 800,482 800,542 280,542" fill="var(--gold)"/>
    <polygon points="280,542 292,542 296,552" fill="var(--gold-dark)"/>
  </svg>

  <div class="abs wordmark front__logo"><span class="wordmark__dot"></span><span class="wordmark__name">Esteban<br>Quintero</span></div>

  <div class="abs name-band">
    <p class="name-band__first">Esteban (9th Grade)</p>
    <p class="name-band__last">QUINTERO!</p>
  </div>

  <p class="abs charge">Walter Cuellar is charged with voter fraud by changing voter addresses from across the RGV so they could vote in Edinburg.</p>

  <div class="abs socials" aria-hidden="true"><span></span><span></span><span></span><span></span></div>
  <p class="abs handle">@Esteban-Quintero-for-Edinburg</p>

  <p class="abs saying-q">WHAT'S THAT FAMOUS SAYING?</p>
  <p class="abs saying">“SHOW ME WHO YOUR FRIENDS ARE AND I'LL<br>TELL YOU WHO YOU REALLY ARE!”</p>
</section>

<section class="card card--back" aria-label="Mailer back">
  <svg class="shapes" width="800" height="560" viewBox="0 0 800 560">
    <defs>
      <linearGradient id="panelTone" x1="0" y1="0" x2="1" y2="1">
        <stop offset="0" stop-color="#1a4c9c"/>
        <stop offset="1" stop-color="#0b2457"/>
      </linearGradient>
    </defs>
    <polygon points="0,0 394,0 436,560 0,560" fill="url(#panelTone)"/>
    <polygon points="394,0 406,0 448,560 436,560" fill="var(--gold)"/>
    <polygon points="0,440 446,440 452,496 0,496" fill="var(--gold)"/>
    <polygon points="446,440 452,496 462,506 456,496" fill="var(--gold-dark)"/>
    <rect x="0" y="496" width="448" height="64" fill="var(--navy)"/>
  </svg>

  <h2 class="abs back__question">Did Esteban (9th Grade) Quintero commit voter fraud when he ran for office in 2016?</h2>

  <div class="abs back__list-photo" role="img" aria-label="Blurred photo of the printed voter list"></div>

  <p class="abs back__intro">Here is a list of people from all over the RGV that voted in Edinburg in the 2016 race.<br>Here is a break down:</p>

  <ul class="abs breakdown">
    <li>- <strong>9 People</strong> voted in Edinburg who were <strong>registered in Donna</strong></li>
    <li>- <strong>13 People</strong> voted in Edinburg who were <strong>registered in San Juan</strong></li>
    <li>- <strong>8 People</strong> voted in Edinburg who were <strong>registered in Pharr</strong></li>
    <li>- <strong>31 People</strong> voted in Edinburg who were <strong>registered in McAllen</strong></li>
    <li>- <strong>2 People</strong> voted in Edinburg who were <strong>registered in La Joya</strong></li>
    <li>- <strong>6 People</strong> voted in Edinburg who were <strong>registered in Edcouch</strong></li>
    <li>- <strong>2 People</strong> voted in Edinburg who were <strong>registered in Mercedes</strong></li>
    <li>- <strong>2 People</strong> voted in Edinburg who were <strong>registered in Monte Alto</strong></li>
    <li>- <strong>6 People</strong> voted in Edinburg who were <strong>registered in Weslaco</strong></li>
    <li>- <strong>1 Person</strong> voted in Edinburg who were <strong>registered in Penitas</strong></li>
    <li>- <strong>3 People</strong> voted in Edinburg who were <strong>registered in Alamo</strong></li>
    <li>- <strong>5 People</strong> voted in Edinburg who were <strong>registered in Elsa</strong></li>
    <li>- <strong>6 People</strong> voted in Edinburg who were <strong>registered in Mission</strong></li>
    <li>- <strong>1 Person</strong> voted in Edinburg who were <strong>registered in Alton</strong></li>
  </ul>

  <p class="abs cheat">WILL ESTEBAN (9TH GRADE) QUINTERO CHEAT IN 2020?<span>Only time will tell...</span></p>
  <p class="abs vote-out">VOTE <em>ESTEBAN (9TH GRADE) QUINTERO</em> OUT OF OFFICE!</p>

  <div class="abs wordmark back__logo"><span class="wordmark__dot"></span><span class="wordmark__name">Esteban<br>Quintero</span></div>
  <div class="abs stamp" aria-label="Postage area"></div>
  <div class="abs address-line" style="top:226px"></div>
  <div class="abs address-line" style="top:274px"></div>
  <div class="abs address-line" style="top:323px"></div>
  <div class="abs address-line" style="top:370px"></div>
</section>

</body>
</html>
```